Flyer for Healthcare Provider -- Sleep Disorders
Sleep Scoring Services
Need Help Scoring
Flyer to be sent out to potential clients
Health
Doctors, healthcare professionals, healthcare administrators, CEOs, sleep lab managers, etc
- Need the flyer to have a strong medical and corporate feel
- Need to sell our services
Text for flyer
Company logo

```html
<!DOCTYPE html>
<html lang="en">
<head>
<meta charset="utf-8">
<title>Restwell Scoring – Flyer Set</title>
<link href="https://fonts.googleapis.com/css2?family=Open+Sans:wght@300;400;600;700&display=swap" rel="stylesheet">
<style>
  :root{
    --stage:#e6e9ed;
    --blue-deep:#0d3f7a;
    --blue-mid:#1a67b3;
    --blue-bright:#2f8ad6;
    --blue-pale:#cfe3f5;
    --ink:#23364d;
    --white:#ffffff;
  }
  *{margin:0;padding:0;box-sizing:border-box}
  html,body{width:1200px;height:835px;overflow:hidden}
  body{background:var(--stage);font-family:"Open Sans",Arial,sans-serif;position:relative}

  /* ---------- front flyer ---------- */
  .flyer-front{position:absolute;left:91px;top:89px;width:447px;height:703px;background:var(--white);overflow:hidden;box-shadow:0 3px 10px rgba(0,0,0,.25)}
  .front-waves{position:absolute;left:0;top:0}
  .hero-photo{position:absolute;left:205px;top:0;width:242px;height:320px;background:radial-gradient(ellipse at 45% 40%,#efd9c6 0%,#d9c2ae 35%,#e8edf2 75%)}
  .team-photo{position:absolute;left:215px;top:345px;width:232px;height:290px;background:linear-gradient(180deg,rgba(210,225,238,.35) 0%,rgba(225,235,244,.6) 50%,rgba(120,170,210,.2) 100%)}
  .headline-tab{position:absolute;left:0;top:22px;width:200px;height:36px;background:var(--blue-mid);border-radius:0 18px 18px 0;color:var(--white);font-weight:700;font-size:17px;line-height:36px;padding-left:12px;white-space:nowrap;z-index:2}
  .intro{position:absolute;left:14px;top:70px;width:188px;color:var(--ink);font-size:6px;line-height:1.4;z-index:2}
  .intro p{margin-bottom:5px}
  .intro ul{list-style:none}
  .intro li{padding-left:7px;position:relative;margin-bottom:1px}
  .intro li::before{content:"";position:absolute;left:1px;top:3px;width:3px;height:3px;border-radius:50%;background:var(--blue-mid)}
  .priority-title{position:absolute;left:16px;top:372px;color:var(--white);font-weight:700;font-size:19px}
  .priority-copy{position:absolute;left:16px;top:402px;width:190px;color:var(--white);font-size:6.2px;line-height:1.45}
  .priority-copy p{margin-bottom:6px}
  .contact{position:absolute;left:16px;top:578px;width:225px;color:var(--white);font-weight:700;font-size:8.5px;line-height:1.5}
  .contact .lead{font-weight:400;font-size:6.5px;text-align:center;margin-bottom:3px}
  .brand{position:absolute;left:16px;top:660px;display:flex;align-items:center;gap:8px;color:var(--white);font-weight:700;font-size:18px}
  .brand-dot{width:22px;height:22px;border-radius:50%;background:var(--white)}
  .offer{position:absolute;left:262px;top:640px;width:175px;text-align:center;color:var(--white);font-size:8px;line-height:1.3}
  .offer strong{display:block;font-size:17px;font-weight:700}
  .offer strong span{font-weight:400}

  /* ---------- back panel ---------- */
  .flyer-back{position:absolute;left:648px;top:91px;width:456px;height:701px;background:linear-gradient(180deg,var(--blue-mid) 0%,var(--blue-deep) 100%);overflow:hidden;box-shadow:0 3px 10px rgba(0,0,0,.25)}
  .fold-card{position:absolute;left:600px;top:612px;width:504px;height:180px;background:linear-gradient(180deg,var(--blue-mid) 0%,var(--blue-deep) 100%);overflow:hidden;box-shadow:0 3px 10px rgba(0,0,0,.35)}
  .discount{position:absolute;left:0;width:100%;text-align:center;color:var(--white);font-size:38px;font-weight:400;letter-spacing:.5px;line-height:1}
  .discount span{font-size:32px}
</style>
</head>
<body>

<section class="flyer-front">
  <svg class="front-waves" width="447" height="703" viewBox="0 0 447 703">
    <defs>
      <linearGradient id="bodyBlue" x1="0" y1="0" x2="0" y2="1">
        <stop offset="0" stop-color="#1f74c2"/>
        <stop offset="1" stop-color="#0d3f7a"/>
      </linearGradient>
    </defs>
    <path d="M0 318 C120 292 300 350 447 305 L447 703 L0 703 Z" fill="#9cc6ea"/>
    <path d="M0 335 C140 310 290 375 447 322 L447 703 L0 703 Z" fill="#4f9ad9"/>
    <path d="M0 355 C150 335 300 390 447 345 L447 703 L0 703 Z" fill="url(#bodyBlue)"/>
    <path d="M0 645 C150 628 300 665 447 635 L447 703 L0 703 Z" fill="#0a2f5d"/>
  </svg>

  <div class="hero-photo" role="img" aria-label="Portrait photo of a smiling healthcare professional"></div>
  <div class="team-photo" role="img" aria-label="Photo of a medical team of doctor and nurses"></div>

  <h1 class="headline-tab">Need help Scoring?</h1>
  <div class="intro">
    <p>Restwell Scoring provides the highest quality and most cost effective scoring services to the sleep medicine industry.</p>
    <p>How do you know when it's time to get a professional scoring service? Below are a few critical signs that your sleep laboratory is ready for a scoring service provider.</p>
    <ul>
      <li>Your sleep laboratory consistently has a backlog of sleep studies</li>
      <li>It takes longer than 3 business days to have sleep studies scored</li>
      <li>You are short staffed – vacations, sick days, maternity and unexpected departures impact productivity</li>
      <li>Your sleep laboratory has limited or no RPSGTs on staff</li>
      <li>It is necessary for your sleep laboratory to reduce and control operating costs</li>
      <li>Quality assurance with internal scorers has been brought into question</li>
    </ul>
  </div>

  <h2 class="priority-title">Priority Scoring</h2>
  <div class="priority-copy">
    <p>For patient records that need rapid scoring attention.</p>
    <p>There are always some patients that require immediate attention. Restwell Scoring PRIORITY SCORING offers same day service to clients in our 24–48 hour turnaround times, so urgent cases can be diagnosed and treated faster with results delivered to referring physicians in record time.</p>
    <p>Restwell Scoring clients include some of the largest sleep disorders laboratories and hospitals in the world. Discover how these labs rely on our trusted team for scoring.</p>
  </div>

  <div class="contact">
    <div class="lead">For a complimentary evaluation of your current scoring requirements call:</div>
    <div>1-800-555-0142 | info@restwellscoring.com</div>
    <div>www.restwellscoring.com</div>
  </div>

  <div class="brand"><span class="brand-dot"></span>Restwell Scoring</div>

  <div class="offer">
    Call today and sign up for a
    <strong>10% DISCOUNT <span>OFF</span></strong>
    your first 10 sleep studies.
  </div>
</section>

<section class="flyer-back">
  <p class="discount" style="top:282px">10% <span>DISCOUNT</span></p>
</section>

<section class="fold-card">
  <p class="discount" style="top:84px">10% <span>DISCOUNT</span></p>
</section>

</body>
</html>
```